electrical automation company needs a letterhead design

we need a letter head designed for our new electrical automation company. Our company color are orange and blue as you'll see from our logo attached

Target Market(s)

Domestic, commercial and industrial electrical clients

Industry/Entity Type

Electrical

Contact Information for Business Card

I need to update my business card to make it more eye catching I have attached my old business card designs, logo and new trifold brochure to give you an idea

Font styles to use
Sans Serif

Colors
f37122
0393ce

Requirements
Must have
• larkfield electrical logo
my name
phone number
email
website
Nice to have
• QR code linked to my website
list of some services
- domestic
- commercial
- industrial

```html
<!DOCTYPE html>
<html lang="en">
<head>
<meta charset="utf-8">
<title>Larkfield Electrical – Letterhead</title>
<link rel="stylesheet" href="https://fonts.googleapis.com/css2?family=Open+Sans:wght@400;600;700&family=Montserrat:wght@700;800&display=swap">
<style>
  :root {
    --brand-blue: #0393ce;
    --brand-orange: #f37122;
    --ink: #333333;
    --body-ink: #6b6b6b;
    --paper: #f7f7f8;
    --backdrop: #e4e5e6;
  }
  * { box-sizing: border-box; margin: 0; padding: 0; }
  html, body {
    width: 1200px;
    height: 945px;
    overflow: hidden;
    background: var(--backdrop);
    font-family: "Open Sans", Arial, sans-serif;
  }
  .letterhead {
    position: absolute;
    left: 280px;
    top: 20px;
    width: 640px;
    height: 905px;
    background: var(--paper);
    box-shadow: 0 2px 10px rgba(0,0,0,0.12);
    overflow: hidden;
  }
  .brand {
    position: absolute;
    left: 48px;
    top: 48px;
    display: flex;
    align-items: center;
    gap: 10px;
  }
  .brand-dot {
    width: 26px;
    height: 26px;
    border-radius: 50%;
    background: var(--brand-orange);
  }
  .brand-name {
    font-family: "Montserrat", Arial, sans-serif;
    font-weight: 800;
    font-size: 19px;
    letter-spacing: 0.5px;
    text-transform: uppercase;
    color: var(--brand-blue);
  }
  .contact {
    position: absolute;
    right: 48px;
    top: 44px;
    text-align: right;
    font-size: 9px;
    line-height: 1.5;
    color: var(--ink);
  }
  .contact-name {
    font-weight: 700;
    color: var(--brand-orange);
    text-transform: uppercase;
  }
  .contact-line {
    display: flex;
    justify-content: flex-end;
    align-items: center;
    gap: 4px;
  }
  .contact-line svg { width: 8px; height: 8px; }
  .letter {
    position: absolute;
    left: 48px;
    top: 176px;
    width: 520px;
  }
  .salutation {
    font-weight: 700;
    font-size: 14px;
    color: var(--ink);
    margin-bottom: 12px;
  }
  .letter p {
    font-size: 11.5px;
    line-height: 1.4;
    color: var(--body-ink);
    margin-bottom: 20px;
  }
  .signature {
    position: absolute;
    left: 48px;
    top: 650px;
    width: 160px;
    height: 58px;
    background: linear-gradient(90deg, #d9d9dc, #ececee);
    border-radius: 3px;
  }
  .footer-band {
    position: absolute;
    left: 0;
    bottom: 0;
    width: 640px;
    height: 70px;
  }
  .footer-band svg { position: absolute; inset: 0; }
  .website {
    position: absolute;
    right: 34px;
    top: 8px;
    font-size: 10px;
    color: #ffffff;
  }
  .services {
    position: absolute;
    left: 48px;
    bottom: 12px;
    display: flex;
    gap: 12px;
    list-style: none;
    font-size: 11px;
    font-weight: 700;
    color: #ffffff;
  }
  .services li::before { content: "• "; }
</style>
</head>
<body>
  <main class="letterhead">
    <header>
      <div class="brand">
        <span class="brand-dot"></span>
        <span class="brand-name">Larkfield Electrical</span>
      </div>
      <div class="contact">
        <div class="contact-name">Dana Porter</div>
        <div class="contact-line">0400 555 018
          <svg viewBox="0 0 10 10" aria-hidden="true"><rect x="2.5" y="0.5" width="5" height="9" rx="1" fill="none" stroke="#f37122" stroke-width="1"/></svg>
        </div>
        <div class="contact-line">dana@larkfield-electrical.com.au
          <svg viewBox="0 0 10 10" aria-hidden="true"><rect x="0.5" y="2" width="9" height="6" fill="none" stroke="#f37122" stroke-width="1"/><path d="M0.5 2 L5 5.5 L9.5 2" fill="none" stroke="#f37122" stroke-width="1"/></svg>
        </div>
      </div>
    </header>

    <section class="letter">
      <h1 class="salutation">Dear Mr. Ellis,</h1>
      <p>Lorem Ipsum is simply dummy text of the printing and typesetting industry. Lorem Ipsum has been the industry's standard dummy text ever since the 1500s, when an unknown printer took a galley of type and scrambled it to make a type specimen book. It has survived not only five centuries, but also the leap into electronic typesetting, remaining essentially unchanged.</p>
      <p>The standard chunk of Lorem Ipsum used since the 1500s is reproduced below for those interested. Sections 1.10.32 and 1.10.33 from "de Finibus Bonorum et Malorum" by Cicero are also reproduced in their exact original form, accompanied by English versions from the 1914 translation by H. Rackham</p>
      <p>Lorem Ipsum is simply dummy text of the printing and typesetting industry. Lorem Ipsum has been the industry's standard dummy text ever since the 1500s, when an unknown printer took a galley of type and scrambled it to make a type specimen book. It has survived not only five centuries, but also the leap into electronic typesetting, remaining essentially unchanged. It was popularised in the</p>
      <p>Lorem Ipsum is simply dummy text of the printing and typesetting industry. Lorem Ipsum has been the industry's standard dummy text ever since the 1500s, when an unknown printer took a galley of type and scrambled it to make a type specimen book. It has survived not only five centuries, but also the leap into electronic typesetting, remaining essentially unchanged. It was popularised in the</p>
    </section>

    <div class="signature" role="img" aria-label="Handwritten signature of the sender"></div>

    <footer class="footer-band">
      <svg viewBox="0 0 640 70" width="640" height="70" aria-hidden="true">
        <path d="M0 34 L640 0 L640 70 L0 70 Z" fill="var(--brand-blue)"/>
        <path d="M370 14 C390 14 395 32 420 30 L590 20 Q600 19 604 6 L372 14 Z" fill="var(--brand-orange)"/>
      </svg>
      <span class="website">www.larkfield-electrical.com.au</span>
      <ul class="services">
        <li>Domestic</li>
        <li>Commercial</li>
        <li>Industrial</li>
      </ul>
    </footer>
  </main>
</body>
</html>
```